Business that Cleans the dishes and utensils used in private jets needs a flyer to describe its b...

I need a flyer to describe a HK based company called 'Vantor Rinsing'. We help the flight attendants to clean valuable dishes and utensils to save them time and costs. Color green is preferable. The design shall be easy to read and clear

Target Market(s)

Flight attendants and flight operations management

Industry/Entity Type

Aviation

Colors

Designer to choose colors to be used in the design.

Requirements
Must have
• Clean and professional.

```html
<!DOCTYPE html>
<html lang="en">
<head>
<meta charset="UTF-8">
<title>Vantor Rinsing – Flyer</title>
<link href="https://fonts.googleapis.com/css2?family=Raleway:wght@800&family=Roboto+Condensed:wght@400;700&display=swap" rel="stylesheet">
<style>
  :root {
    --page-bg: #e3e4e6;
    --green-light: #8cc63f;
    --green-mid: #62b445;
    --green-deep: #21532a;
    --green-band: #4f8a36;
    --brand-yellow: #f5e916;
    --bar-yellow: #ffeb00;
    --ink-dark: #1b3d20;
    --ink-black: #111;
    --white: #ffffff;
    --plate: #e4eef4;
  }
  * { margin: 0; padding: 0; box-sizing: border-box; }
  html, body {
    width: 1200px; height: 1200px; overflow: hidden;
    background: var(--page-bg);
  }
  .flyer {
    position: absolute; left: 220px; top: 108px;
    width: 760px; height: 984px; overflow: hidden;
    background: var(--green-mid);
    box-shadow: 8px 10px 18px rgba(0,0,0,.25);
  }
  .flyer-shapes { position: absolute; inset: 0; }
  .brand-name {
    position: absolute; left: 70px; top: 150px; width: 380px;
    font-family: "Raleway", sans-serif; font-weight: 800;
    font-size: 42px; line-height: 1; color: var(--brand-yellow);
    text-align: center; white-space: nowrap;
  }
  .hero-plates {
    position: absolute; left: 472px; top: 90px; width: 250px; height: 180px;
    border-radius: 50%;
    background: var(--plate);
    border: 6px solid var(--white);
  }
  .scene-backdrop {
    position: absolute; left: 0; top: 360px; width: 760px; height: 220px;
    background: linear-gradient(180deg, rgba(140,198,63,0) 0%, rgba(140,198,63,.55) 60%, rgba(140,198,63,.8) 100%);
  }
  .headline {
    position: absolute; left: 0; top: 372px; width: 760px;
    font-family: "Raleway", sans-serif; font-weight: 800;
    font-size: 36px; line-height: 46px; color: var(--white);
    text-align: center;
  }
  .intro {
    position: absolute; left: 0; top: 472px; width: 760px;
    font-family: "Roboto Condensed", sans-serif; font-weight: 400;
    font-size: 22px; line-height: 30px; color: var(--ink-black);
    text-align: center;
  }
  .badge-plates {
    position: absolute; left: 345px; top: 580px; width: 88px; height: 66px;
    border-radius: 50%;
    background: var(--plate);
    border: 3px solid var(--white);
  }
  .subheads {
    position: absolute; left: 0; top: 672px; width: 760px;
    font-family: "Roboto Condensed", sans-serif; font-weight: 400;
    font-size: 24px; line-height: 30px; color: var(--white);
    text-align: center;
  }
  .body-copy {
    position: absolute; left: 70px; top: 756px; width: 620px;
    font-family: "Roboto Condensed", sans-serif; font-weight: 400;
    font-size: 14.5px; line-height: 19.5px; color: var(--white);
    text-align: center;
  }
  .contact-bar {
    position: absolute; left: 0; top: 873px; width: 760px; height: 73px;
    background: var(--bar-yellow);
    display: flex; align-items: center; justify-content: center; gap: 14px;
    font-family: "Roboto Condensed", sans-serif; font-size: 33px; color: var(--ink-dark);
  }
  .contact-phone { font-weight: 700; }
  .contact-divider { font-weight: 400; }
  .contact-web { font-weight: 400; }
</style>
</head>
<body>
<main class="flyer">
  <svg class="flyer-shapes" viewBox="0 0 760 984" width="760" height="984" aria-hidden="true">
    <defs>
      <linearGradient id="topPanel" x1="0" y1="0" x2="0" y2="1">
        <stop offset="0" stop-color="#66b846"/>
        <stop offset=".55" stop-color="#3f8b35"/>
        <stop offset="1" stop-color="#1f5228"/>
      </linearGradient>
      <linearGradient id="swoosh" x1="1" y1="0" x2="0" y2="1">
        <stop offset="0" stop-color="#ffffff" stop-opacity="1"/>
        <stop offset=".5" stop-color="#ffffff" stop-opacity=".6"/>
        <stop offset="1" stop-color="#ffffff" stop-opacity="0"/>
      </linearGradient>
      <linearGradient id="midField" x1="0" y1="0" x2="0" y2="1">
        <stop offset="0" stop-color="#62b445"/>
        <stop offset="1" stop-color="#8cc63f"/>
      </linearGradient>
    </defs>
    <rect x="0" y="0" width="760" height="984" fill="url(#midField)"/>
    <path d="M0,0 H700 C660,180 520,332 360,332 C220,332 90,292 0,228 Z" fill="url(#topPanel)"/>
    <path d="M0,232 C100,300 230,345 370,345 C520,345 640,250 700,140 C660,270 520,352 370,352 C220,352 90,310 0,240 Z" fill="#ffffff" fill-opacity=".7"/>
    <path d="M700,0 H760 V140 C700,250 600,320 470,345 C590,300 680,170 700,0 Z" fill="url(#swoosh)"/>
    <path d="M0,640 C200,560 560,540 760,620 V984 H0 Z" fill="var(--green-band)"/>
    <path d="M0,658 C220,570 560,560 760,650 V984 H0 Z" fill="var(--green-deep)"/>
  </svg>

  <div class="scene-backdrop" role="img" aria-label="Faint airport terminal scene with a plane, seating and city skyline"></div>
  <div class="brand-name">Vantor Rinsing</div>
  <div class="hero-plates" role="img" aria-label="Illustration of two clean dinner plates with a clock face and sparkles"></div>

  <h1 class="headline">THE BEST WAY TO<br>CLEAN DISHES</h1>
  <p class="intro">We help the flight attendants to clean<br>valuable dishes and utensils to save them time and costs</p>

  <div class="badge-plates" role="img" aria-label="Small icon of two clean plates with sparkles"></div>

  <h2 class="subheads">Streamline the Process to Make Washing Dishes Manageable<br>The Best Way to Clean Dishes by Hand</h2>
  <p class="body-copy">If you’re faced with an enormous stack of dirty flatware and cooking utensils, it’s going to take longer to get all of your dishes clean. It’s also tempting to put the task off, which means the dishes keep piling up. Saving all your washing for later is stressful and not the best way to clean dishes.</p>

  <div class="contact-bar">
    <span class="contact-phone">852 5550 1942</span>
    <span class="contact-divider">|</span>
    <span class="contact-web">www.vantorrinsing.com</span>
  </div>
</main>
</body>
</html>
```